Harbor Print Studio gallery website

I need a Website for a gallery with a shopify integration or maybe even better also compatible with squarespace.
the website should have following riders: Künstler, Veranstaltungen, Shop, About Us.
some nice examples for inspiration of the website architecture are:
https://www.tarnelgalerie.com/
https://www.mossline-gallery.com/de/
https://zinnbergalerie.de/
It should be easy for us to make adaptations and fill the website with new content.
Attached there is the CI an logo for the brand.
Art Collectors,
artgallery
3 page

```html
<!DOCTYPE html>
<html lang="en">
<head>
<meta charset="utf-8">
<title>Harbor Print Studio – Shop</title>
<link href="https://fonts.googleapis.com/css2?family=Montserrat:wght@300;400&family=Roboto:wght@400;500;700&display=swap" rel="stylesheet">
<style>
:root{
  --red:#c3161c;
  --ink:#111111;
  --muted:#666666;
  --paper:#ffffff;
  --soft:#f4f4f4;
  --footer:#1b1b1b;
  --footer-line:#3a3a3a;
}
*{box-sizing:border-box;margin:0;padding:0}
html,body{width:1200px;height:3474px;overflow:hidden}
body{position:relative;background:var(--paper);font-family:'Roboto',sans-serif;color:var(--ink)}

/* header */
.site-header{position:absolute;left:0;top:0;width:1200px;height:86px;background:var(--paper);z-index:3}
.brand-plate{position:absolute;left:144px;top:0;width:294px;height:167px;background:var(--paper);
  clip-path:polygon(0 0,100% 0,100% 52%,80% 100%,20% 100%,0 52%);z-index:4}
.brand-name{position:absolute;left:0;top:100px;width:294px;text-align:center;font-family:'Montserrat',sans-serif;font-weight:300;font-size:20px;color:var(--ink);text-transform:uppercase;letter-spacing:.2px;white-space:nowrap}
.main-nav{position:absolute;top:36px;left:0;font-size:13px;font-weight:500;text-transform:uppercase}
.main-nav a{position:absolute;white-space:nowrap;color:var(--ink);text-decoration:none}
.main-nav a.is-active{color:var(--red)}
.main-nav a.is-active::before{content:"";position:absolute;left:50%;top:-16px;width:7px;height:7px;margin-left:-4px;border-radius:50%;background:var(--red)}
.header-icons{position:absolute;top:33px;left:978px;display:flex;gap:10px}
.header-icons svg{width:18px;height:18px}

/* hero */
.hero{position:absolute;left:0;top:86px;width:1200px;height:472px;
  background:linear-gradient(180deg,#3b3a38 0%,#8a857e 45%,#b9b3aa 70%,#d6d1ca 100%)}
.hero-overlay{position:absolute;inset:0;background:rgba(20,18,16,.32)}
.hero-title{position:absolute;top:148px;left:0;width:1200px;text-align:center;font-family:'Montserrat',sans-serif;font-weight:300;font-size:41px;color:#fff;letter-spacing:1px}
.hero-text{position:absolute;top:204px;left:0;width:1200px;text-align:center;font-size:15.5px;line-height:23px;color:#fff;font-weight:500}
.btn-shop{position:absolute;left:526px;top:271px;width:148px;height:42px;background:var(--red);color:#fff;font-weight:700;font-size:15px;
  display:flex;align-items:center;justify-content:center;gap:7px;text-transform:uppercase;text-decoration:none}

/* product grid */
.product-grid{position:absolute;left:143px;top:647px;display:grid;grid-template-columns:repeat(3,280px);column-gap:36px;grid-auto-rows:421px}
.product-card{position:relative;width:280px;text-align:center}
.product-frame{width:280px;height:280px;border:10px solid #000;padding:12px;background:#fff}
.artwork{width:100%;height:100%}
.product-cat{position:absolute;top:308px;left:0;width:280px;font-size:12.5px;color:var(--muted);text-transform:uppercase;letter-spacing:.3px}
.product-name{position:absolute;top:327px;left:0;width:280px;font-size:17.5px;font-weight:500}
.product-price{position:absolute;top:362px;left:0;width:280px;font-size:15px;font-weight:700;color:var(--red)}

/* pagination */
.pagination{position:absolute;top:2770px;left:480px;display:flex;gap:10px}
.page{width:40px;height:40px;border-radius:50%;background:#fff;box-shadow:0 4px 12px rgba(0,0,0,.14);display:flex;align-items:center;justify-content:center;font-size:14px;font-weight:500;color:var(--ink)}
.page.is-current{background:var(--red);color:#fff}

/* follow */
.follow{position:absolute;left:0;top:2902px;width:1200px;height:118px;background:var(--soft)}
.follow-title{position:absolute;top:42px;left:0;width:1200px;display:flex;justify-content:center;align-items:center;gap:14px;font-family:'Montserrat',sans-serif;font-size:38px;font-weight:400;letter-spacing:1px}
.follow-title i{display:block;width:30px;height:30px;border:3px solid var(--red);border-radius:8px}
.feed{position:absolute;left:0;top:3020px;width:1200px;height:175px;display:flex}
.feed div{flex:1}

/* footer */
.site-footer{position:absolute;left:0;top:3195px;width:1200px;height:279px;background:var(--footer);color:#fff}
.f-col{position:absolute;top:52px}
.f-col h4{font-size:15.5px;font-weight:500;text-transform:uppercase;margin-bottom:16px}
.f-col ul{list-style:none;font-size:11px;line-height:21px}
.f-divider{position:absolute;top:44px;width:1px;height:147px;background:var(--footer-line)}
.contact-row{display:flex;align-items:flex-start;gap:11px;font-size:11px;line-height:14px;margin-bottom:13px}
.contact-row svg{width:13px;height:13px;flex:none}
.contact-row a{color:#fff}
.social-row{display:flex;align-items:center;gap:12px;font-size:11px;margin-bottom:9px}
.social-row span{width:28px;height:28px;border-radius:50%;background:var(--red);display:block}
.f-rule{position:absolute;left:144px;top:225px;width:912px;height:1px;background:var(--footer-line)}
.copyright{position:absolute;top:246px;left:0;width:1200px;text-align:center;font-size:10px}
</style>
</head>
<body>

<header class="site-header">
  <nav class="main-nav">
    <a style="left:503px" href="#">Home</a>
    <a style="left:565px" href="#">Artists</a>
    <a style="left:643px" href="#">Events</a>
    <a style="left:716px" class="is-active" href="#">Shop</a>
    <a style="left:775px" href="#">About Us</a>
    <a style="left:863px" href="#">Contact Us</a>
  </nav>
  <div class="header-icons">
    <svg viewBox="0 0 20 20" fill="none" stroke="#111" stroke-width="1.8"><circle cx="10" cy="6.5" r="3.8"/><path d="M3 18c0-4 3-6 7-6s7 2 7 6z"/></svg>
    <svg viewBox="0 0 20 20" fill="none" stroke="#111" stroke-width="2"><circle cx="8.5" cy="8.5" r="5.5"/><path d="M12.5 12.5l5 5"/></svg>
    <svg viewBox="0 0 20 20" fill="none" stroke="#111" stroke-width="1.8"><path d="M10 17.5S2.5 12.5 2.5 7.2A4 4 0 0 1 10 5a4 4 0 0 1 7.5 2.2C17.5 12.5 10 17.5 10 17.5z"/></svg>
  </div>
</header>
<div class="brand-plate">
  <span class="brand-name">Harbor Print Studio</span>
</div>

<section class="hero" role="img" aria-label="Gallery interior with framed paintings and sculptures on plinths">
  <div class="hero-overlay"></div>
  <h1 class="hero-title">OUR SHOP</h1>
  <p class="hero-text">Lorem ipsum dolor sit amet, consectetur adipiscing elit, sed<br>incididunt ut labore et dolore magna aliqua.</p>
  <a class="btn-shop" href="#">Shop Now
    <svg width="15" height="15" viewBox="0 0 16 16"><circle cx="8" cy="8" r="7.5" fill="#fff"/><path d="M6.5 4.5L10 8l-3.5 3.5" stroke="#c3161c" stroke-width="2" fill="none"/></svg>
  </a>
</section>

<main class="product-grid">
  <article class="product-card"><div class="product-frame"><div class="artwork" role="img" aria-label="Swirling night sky painting over a village" style="background:linear-gradient(160deg,#2c4f9c,#5a7fc2 45%,#1f2f5a)"></div></div><p class="product-cat">Prints</p><h3 class="product-name">Lorem ipsum dolor sit amet</h3><p class="product-price">€2300</p></article>
  <article class="product-card"><div class="product-frame"><div class="artwork" role="img" aria-label="Colourful impasto avenue of trees by water" style="background:linear-gradient(135deg,#e7842e,#a44bc4 50%,#5b6ed8)"></div></div><p class="product-cat">Prints</p><h3 class="product-name">Lorem ipsum dolor sit amet</h3><p class="product-price">€2300</p></article>
  <article class="product-card"><div class="product-frame"><div class="artwork" role="img" aria-label="Colourful painted dog portrait" style="background:radial-gradient(circle at 50% 55%,#473a6c,#8ab7d6 60%,#e8f4f8)"></div></div><p class="product-cat">Prints</p><h3 class="product-name">Lorem ipsum dolor sit amet</h3><p class="product-price">€2300</p></article>

  <article class="product-card"><div class="product-frame"><div class="artwork" role="img" aria-label="Tall ship sailing on rough sea" style="background:linear-gradient(180deg,#e8dcc0,#c9b88f 50%,#3f7a78)"></div></div><p class="product-cat">Prints</p><h3 class="product-name">Lorem ipsum dolor sit amet</h3><p class="product-price">€2300</p></article>
  <article class="product-card"><div class="product-frame"><div class="artwork" role="img" aria-label="Rainy city street with clock tower" style="background:linear-gradient(180deg,#8a8d96,#6b6058 55%,#3d3530)"></div></div><p class="product-cat">Prints</p><h3 class="product-name">Lorem ipsum dolor sit amet</h3><p class="product-price">€2300</p></article>
  <article class="product-card"><div class="product-frame"><div class="artwork" role="img" aria-label="Poppies and daisies on a blue background" style="background:linear-gradient(180deg,#2c6d9c,#3b8a8a 55%,#4f7a2e)"></div></div><p class="product-cat">Prints</p><h3 class="product-name">Lorem ipsum dolor sit amet</h3><p class="product-price">€2300</p></article>

  <article class="product-card"><div class="product-frame"><div class="artwork" role="img" aria-label="Purple and orange painted avenue" style="background:linear-gradient(135deg,#d45a2a,#8e46c0 50%,#6a86e0)"></div></div><p class="product-cat">Prints</p><h3 class="product-name">Lorem ipsum dolor sit amet</h3><p class="product-price">€2300</p></article>
  <article class="product-card"><div class="product-frame"><div class="artwork" role="img" aria-label="Boat floating through fiery clouds" style="background:linear-gradient(180deg,#1f2430,#b5552a 45%,#e3a04a 70%,#3b3a3a)"></div></div><p class="product-cat">Prints</p><h3 class="product-name">Lorem ipsum dolor sit amet</h3><p class="product-price">€2300</p></article>
  <article class="product-card"><div class="product-frame"><div class="artwork" role="img" aria-label="Colourful painted animal portrait" style="background:linear-gradient(135deg,#2a9a8e,#5c3f8c 50%,#e2562c)"></div></div><p class="product-cat">Prints</p><h3 class="product-name">Lorem ipsum dolor sit amet</h3><p class="product-price">€2300</p></article>

  <article class="product-card"><div class="product-frame"><div class="artwork" role="img" aria-label="Figure leaping over a colourful abstract city" style="background:linear-gradient(160deg,#8fc7e8,#9a5fd0 55%,#e2488a)"></div></div><p class="product-cat">Prints</p><h3 class="product-name">Lorem ipsum dolor sit amet</h3><p class="product-price">€2300</p></article>
  <article class="product-card"><div class="product-frame"><div class="artwork" role="img" aria-label="White daisies on deep blue" style="background:linear-gradient(180deg,#1c5fa0,#2a7fb8 50%,#17467a)"></div></div><p class="product-cat">Prints</p><h3 class="product-name">Lorem ipsum dolor sit amet</h3><p class="product-price">€2300</p></article>
  <article class="product-card"><div class="product-frame"><div class="artwork" role="img" aria-label="Lit houses reflected in a canal at dusk" style="background:linear-gradient(180deg,#3c5a52,#6a5030 45%,#1f7d7a)"></div></div><p class="product-cat">Prints</p><h3 class="product-name">Lorem ipsum dolor sit amet</h3><p class="product-price">€2300</p></article>

  <article class="product-card"><div class="product-frame"><div class="artwork" role="img" aria-label="Stag in a misty watercolour landscape" style="background:linear-gradient(180deg,#8a9a8a,#b89a6e 60%,#e2d2a8)"></div></div><p class="product-cat">Prints</p><h3 class="product-name">Lorem ipsum dolor sit amet</h3><p class="product-price">€2300</p></article>
  <article class="product-card"><div class="product-frame"><div class="artwork" role="img" aria-label="Impressionist figure painting in warm tones" style="background:linear-gradient(160deg,#e8d4c0,#c8907a 50%,#8e5a50)"></div></div><p class="product-cat">Prints</p><h3 class="product-name">Lorem ipsum dolor sit amet</h3><p class="product-price">€2300</p></article>
  <article class="product-card"><div class="product-frame"><div class="artwork" role="img" aria-label="Flowering tree over a white coastal house" style="background:linear-gradient(180deg,#b03a5a,#3e7a4a 45%,#e8ecef)"></div></div><p class="product-cat">Prints</p><h3 class="product-name">Lorem ipsum dolor sit amet</h3><p class="product-price">€2300</p></article>
</main>

<nav class="pagination" aria-label="Pages">
  <span class="page is-current">1</span><span class="page">2</span><span class="page">3</span><span class="page">4</span><span class="page">5</span>
</nav>

<section class="follow">
  <h2 class="follow-title"><i></i>FOLLOW US</h2>
</section>
<div class="feed">
  <div role="img" aria-label="Poppies painting" style="background:linear-gradient(160deg,#2e6a8a,#c2402a 55%,#3f6a2a)"></div>
  <div role="img" aria-label="Harbour with sailboats painting" style="background:linear-gradient(180deg,#6fa8d8,#c77ab0 60%,#3c78b8)"></div>
  <div role="img" aria-label="Venetian canal painting" style="background:linear-gradient(180deg,#c9a06a,#8c5a3a 50%,#5a7a4a)"></div>
  <div role="img" aria-label="Daisies painting" style="background:linear-gradient(160deg,#6a7a3a,#d8c070 50%,#4a5a2a)"></div>
  <div role="img" aria-label="Colourful horses painting" style="background:linear-gradient(135deg,#1e2a5a,#d85a2a 50%,#2a3a8a)"></div>
  <div role="img" aria-label="Abstract bird painting" style="background:linear-gradient(135deg,#e85ab0,#f0a0c8 45%,#5ac0e0)"></div>
</div>

<footer class="site-footer">
  <div class="f-col" style="left:144px"><h4>Quick Links</h4>
    <ul><li>Home</li><li>Artists</li><li>Events</li><li>Shop</li><li>About Us.</li></ul></div>
  <div class="f-divider" style="left:291px"></div>
  <div class="f-col" style="left:365px"><h4>Information</h4>
    <ul><li>Terms &amp; Conditions</li><li>Privacy Policy</li><li>Disclaimer</li><li>Site Map</li><li>Contact Us</li><li>Categories</li></ul></div>
  <div class="f-divider" style="left:539px"></div>
  <div class="f-col" style="left:613px"><h4>Contact Info</h4>
    <div class="contact-row"><svg viewBox="0 0 14 14"><path fill="#c3161c" d="M3 1l2 3-1.3 1.3a8 8 0 0 0 4 4L9 8l3 2-1 3C6 13 1 8 1 3z"/></svg>(415) 702-3381</div>
    <div class="contact-row"><svg viewBox="0 0 14 14"><rect x="3" y="1" width="8" height="4" fill="#c3161c"/><rect x="1" y="5" width="12" height="5" rx="1" fill="#c3161c"/><rect x="3" y="9" width="8" height="4" fill="#c3161c"/></svg>(415) 702-3381</div>
    <div class="contact-row"><svg viewBox="0 0 14 14"><rect x="1" y="3" width="12" height="8" fill="#c3161c"/><path d="M1 3l6 5 6-5" stroke="#1b1b1b" fill="none"/></svg><a>hello@harborprint.com</a></div>
    <div class="contact-row"><svg viewBox="0 0 14 14"><path fill="#c3161c" d="M7 1a4.5 4.5 0 0 0-4.5 4.5C2.5 9 7 13 7 13s4.5-4 4.5-7.5A4.5 4.5 0 0 0 7 1z"/><circle cx="7" cy="5.5" r="1.6" fill="#1b1b1b"/></svg><span>#2868 Lorem ipsum dolor sit<br>amet, consectetur</span></div>
  </div>
  <div class="f-divider" style="left:856px"></div>
  <div class="f-col" style="left:929px"><h4>Follow Us</h4>
    <div class="social-row"><span></span>Friendwall</div>
    <div class="social-row"><span></span>Chirpline</div>
    <div class="social-row"><span></span>Orbit Plus</div>
    <div class="social-row"><span></span>Worknet</div>
  </div>
  <div class="f-rule"></div>
  <p class="copyright">Copyrights © The Company name 2024 | Allrights Reserved</p>
</footer>

</body>
</html>
```